Velisa Seafood Shipping Packaging Re-Design

We need a packaging (Shipping Carton) design for our Seafood Products (FROZEN). We already have a basic packaging design which we prefer to have a modern touch on it.
Spec :
1. It must show our logo (Attached), note that the text of "VELISA" which accompany the logo is optional, it can be omitted & showing only the logo.
2. Main color is Blue
3. Our carton is regular shipping box with dimension L43cm x W 27cm x H 16cm.
4. Our material of Carton is both Brown & White Kraft Paperboard, so the design should look nice in both material.

Attached our Logo and packaging design.

Target Market(s)

Frozen Seafood Distributor & Seafood Buyer

Industry/Entity Type

Food Production

Requirements
Must have
• 1. Must Show our Logo
• 2. Main Color of the Text/Logo is Blue
• 3. On the side of the packaging / Carton must show two box of CODE & SIZE
• 4. Must Show these icons :
• a. Handle with Care
• b. Maximum Stackable 10 Carton
• c. Recyleable Material
• d. Protect from the Water/Rain
Nice to have
• Would prefer to have a modern design

```html
<!DOCTYPE html>
<html lang="en">
<head>
<meta charset="utf-8">
<title>Velisa Shipping Carton Dieline</title>
<link rel="stylesheet" href="https://fonts.googleapis.com/css2?family=Cinzel:wght@500&family=Tinos&display=swap">
<style>
  :root {
    --brand-blue: #0f72b5;
    --brand-navy: #1c3d86;
    --teal: #68c3bb;
    --wave-grey: #eeeff1;
    --wave-grey-light: #f6f6f7;
    --fold-line: #e2e2e4;
    --paper: #ffffff;
  }
  * { margin: 0; padding: 0; box-sizing: border-box; }
  html, body { width: 1200px; height: 1000px; overflow: hidden; background: var(--paper); }
  .canvas { position: relative; width: 1200px; height: 1000px; background: var(--paper); }
  .wave-texture {
    position: absolute;
    background: linear-gradient(180deg, var(--wave-grey-light), var(--wave-grey));
  }
  .fold-line { position: absolute; width: 1px; background: var(--fold-line); }
  .brand-name {
    font-family: "Cinzel", "Times New Roman", serif;
    font-weight: 500; letter-spacing: 2px; color: var(--brand-navy); line-height: 1;
    white-space: nowrap;
  }
  .top-band {
    position: absolute; left: 835px; top: 103px; width: 365px; height: 37px;
    background: var(--brand-blue);
    display: flex; align-items: center; justify-content: center;
  }
  .top-band .brand-name { color: var(--paper); font-size: 25px; }
  .brand-disc {
    position: absolute; top: 236px; width: 80px; height: 80px;
    border-radius: 50%; background: var(--brand-blue);
  }
  .front-wordmark {
    position: absolute; top: 312px; width: 220px; height: 36px;
    text-align: center; font-size: 34px;
  }
  .flap-disc {
    position: absolute; left: 375px; top: 117px; width: 86px; height: 86px;
    border-radius: 50%; background: var(--teal);
    display: flex; align-items: center; justify-content: center;
  }
  .flap-disc .brand-name { color: var(--paper); font-size: 14px; letter-spacing: 1px; }
  .teal-stripe { position: absolute; top: 326px; height: 15px; background: var(--teal); }
  .info-box {
    position: absolute; top: 243px; width: 76px; height: 67px;
    border: 2px solid var(--teal); border-top: none; border-radius: 0 0 6px 6px;
    background: var(--paper);
  }
  .info-box .label {
    height: 15px; margin: 0 -2px; background: var(--brand-blue);
    color: var(--paper); font-family: "Tinos", "Times New Roman", serif;
    font-size: 11px; line-height: 15px; padding-left: 8px;
  }
  .care-icons {
    position: absolute; top: 321px; width: 116px; height: 26px;
    background: var(--brand-blue); border-radius: 6px 0 0 6px;
    display: flex; align-items: center; justify-content: flex-end; gap: 4px; padding-right: 14px;
  }
  .care-icons svg { width: 17px; height: 17px; display: block; }
</style>
</head>
<body>
<main class="canvas">

  <div class="wave-texture" role="img" aria-label="Soft grey wave pattern" style="left:0;top:218px;width:233px;height:127px"></div>
  <div class="wave-texture" role="img" aria-label="Soft grey wave pattern" style="left:233px;top:103px;width:370px;height:242px"></div>
  <div class="wave-texture" role="img" aria-label="Soft grey wave pattern" style="left:603px;top:218px;width:232px;height:127px"></div>
  <div class="wave-texture" role="img" aria-label="Soft grey wave pattern" style="left:835px;top:140px;width:365px;height:205px"></div>

  <div class="fold-line" style="left:233px;top:103px;height:369px"></div>
  <div class="fold-line" style="left:603px;top:103px;height:369px"></div>
  <div class="fold-line" style="left:835px;top:103px;height:369px"></div>

  <div class="top-band"><span class="brand-name">VELISA</span></div>

  <div class="flap-disc"><span class="brand-name">VELISA</span></div>

  <div class="teal-stripe" style="left:0;width:117px"></div>
  <div class="teal-stripe" style="left:525px;width:193px"></div>
  <div class="teal-stripe" style="left:835px;width:102px"></div>
  <div class="teal-stripe" style="left:1128px;width:72px"></div>

  <div class="brand-disc" style="left:378px"></div>
  <div class="front-wordmark brand-name" style="left:308px">VELISA</div>
  <div class="brand-disc" style="left:984px"></div>
  <div class="front-wordmark brand-name" style="left:914px">VELISA</div>

  <div class="info-box" style="left:24px"><div class="label">CODE</div></div>
  <div class="info-box" style="left:125px"><div class="label">SIZE</div></div>
  <div class="care-icons" style="left:117px">
    <svg viewBox="0 0 20 20" aria-label="Keep dry"><rect width="20" height="20" fill="#fff"/><path d="M3 10a7 6 0 0 1 14 0z M10 10v6a1.5 1.5 0 0 1-3 0" fill="none" stroke="#0f72b5" stroke-width="1.5"/></svg>
    <svg viewBox="0 0 20 20" aria-label="Handle with care"><rect width="20" height="20" fill="#fff"/><path d="M7 3h6l-1 6h-4z M10 9v5 M4 12l3 5h6l3-5" fill="none" stroke="#0f72b5" stroke-width="1.5"/></svg>
    <svg viewBox="0 0 20 20" aria-label="Stack maximum 10"><rect width="20" height="20" fill="#fff"/><text x="10" y="9" text-anchor="middle" font-size="7" font-family="Arial, sans-serif" fill="#0f72b5">10</text><path d="M4 12h12 M4 15h12" stroke="#0f72b5" stroke-width="1.5"/></svg>
    <svg viewBox="0 0 20 20" aria-label="Recyclable"><rect width="20" height="20" fill="#fff"/><g fill="none" stroke="#0f72b5" stroke-width="1.4"><path d="M8.6 4.2 6 8.6"/><path d="M11.4 4.2 14 8.6"/><path d="M15 12 13 15.5H8"/><path d="M5 12 7 15.5"/></g><g fill="#0f72b5"><path d="M4.6 7.6l3 0.6-0.9 2.6z"/><path d="M14.6 6.8l0.6 3-2.8-0.3z"/><path d="M9 13.6v3.8l-2.4-1.9z"/></g></svg>
  </div>

  <div class="info-box" style="left:627px"><div class="label">CODE</div></div>
  <div class="info-box" style="left:728px"><div class="label">SIZE</div></div>
  <div class="care-icons" style="left:719px">
    <svg viewBox="0 0 20 20" aria-label="Keep dry"><rect width="20" height="20" fill="#fff"/><path d="M3 10a7 6 0 0 1 14 0z M10 10v6a1.5 1.5 0 0 1-3 0" fill="none" stroke="#0f72b5" stroke-width="1.5"/></svg>
    <svg viewBox="0 0 20 20" aria-label="Handle with care"><rect width="20" height="20" fill="#fff"/><path d="M7 3h6l-1 6h-4z M10 9v5 M4 12l3 5h6l3-5" fill="none" stroke="#0f72b5" stroke-width="1.5"/></svg>
    <svg viewBox="0 0 20 20" aria-label="Stack maximum 10"><rect width="20" height="20" fill="#fff"/><text x="10" y="9" text-anchor="middle" font-size="7" font-family="Arial, sans-serif" fill="#0f72b5">10</text><path d="M4 12h12 M4 15h12" stroke="#0f72b5" stroke-width="1.5"/></svg>
    <svg viewBox="0 0 20 20" aria-label="Recyclable"><rect width="20" height="20" fill="#fff"/><g fill="none" stroke="#0f72b5" stroke-width="1.4"><path d="M8.6 4.2 6 8.6"/><path d="M11.4 4.2 14 8.6"/><path d="M15 12 13 15.5H8"/><path d="M5 12 7 15.5"/></g><g fill="#0f72b5"><path d="M4.6 7.6l3 0.6-0.9 2.6z"/><path d="M14.6 6.8l0.6 3-2.8-0.3z"/><path d="M9 13.6v3.8l-2.4-1.9z"/></g></svg>
  </div>

</main>
</body>
</html>
```